15 ft high by 10 ft wide road side sign

road side sign - this is a dual carrigeway speeds of 40 mph so eye time to see ,read and absorb very short is less than 3 seconds 45,000 vehicles a day go past these are local to us our most profitable business is customers instore we embroider company and club and school logos and badges one mile ahead of this sign we have over 400,000 logos we have sewn and are on our servers we are well know in our area we can sew your logo in under 2 hours if it is already on our server we have a fast track service which we charge extra for very profitable is the customers buying items on tradora and bidlot we can really be fast on your own items if you bring them instore we have 15 large multi head machine to cope no one else is that fast on line embroidery takes 7 -10 days we have purchased from others saying 24 hours when put to the test they fail and give excusses why it cannot be do every time we have brought and our customers say the same project your logo embrodery one mile ahead ------- road side sign 15 ft high 10 feet wide company name Harrow Stitch & Embrodery 12 Corvel way EN4 7TR like drivers to be able to drop off and collect sameday because driving you have very very little time to read has to be simple good thing is its a major commutor route A10 Enfield so drivers can be trained via repeat reading dale fenwick

Target Market(s)

our local area is our most profitable market getting people instore online is to slow to for our custopmers and low a margin for us 1,000,000 people withing 2 miles of our store

Industry/Entity Type

Embroidery

Font styles to use
Sans Serif

Colors

Designer to choose colors to be used in the design.

Requirements
Must have
• simple easy to read
• also
• nigel pratley lovers he has NP sewn on his union jack boxer shorts
• as clothing with your company logo are 100% tax deductable for most companies
• as promotional wear
Should not have
• to complicated to read and understand so many people driving past are not english readers as there main language

```html
<!DOCTYPE html>
<html lang="en">
<head>
<meta charset="utf-8">
<title>Harrow Stitch &amp; Embroidery – Roadside Sign</title>
<link rel="stylesheet" href="https://fonts.googleapis.com/css2?family=Arimo:wght@700&display=swap">
<style>
  :root {
    --backdrop: #b0adad;
    --sign-white: #ffffff;
    --band-red: #ff0000;
    --band-navy: #332877;
    --panel-green: #076d47;
  }
  html, body {
    margin: 0;
    padding: 0;
    width: 1200px;
    height: 826px;
    overflow: hidden;
    background: var(--backdrop);
  }
  .roadside-sign {
    display: block;
    width: 1200px;
    height: 826px;
  }
  .sign-text {
    font-family: "Arimo", "Liberation Sans", Arial, sans-serif;
    font-weight: 700;
    fill: var(--sign-white);
  }
  .centred { text-anchor: middle; }
  .sign-border { fill: var(--sign-white); }
  .band-name { fill: var(--band-red); }
  .band-trade { fill: var(--band-navy); }
  .panel-message { fill: var(--panel-green); }
  .icon-white { fill: var(--sign-white); }
  .icon-cut { fill: var(--panel-green); }
</style>
</head>
<body>
<svg class="roadside-sign" viewBox="0 0 1200 826" xmlns="http://www.w3.org/2000/svg" role="img" aria-label="Portrait roadside sign, 10 ft wide by 15 ft high: Harrow Stitch and Embroidery, your logo embroidery one mile ahead, 12 Corvel way EN4 7TR">
  <defs>
    <clipPath id="inner-panel">
      <rect x="351" y="33" width="498" height="760" rx="26" ry="26"/>
    </clipPath>
  </defs>

  <!-- White sign border, 10:15 portrait -->
  <rect class="sign-border" x="338" y="20" width="524" height="786" rx="36" ry="36"/>

  <!-- Colour bands -->
  <g clip-path="url(#inner-panel)">
    <rect class="band-name" x="351" y="33" width="498" height="222"/>
    <rect class="band-trade" x="351" y="255" width="498" height="90"/>
    <rect class="panel-message" x="351" y="345" width="498" height="448"/>
  </g>

  <!-- Company name -->
  <text class="sign-text centred company-name" x="600" y="125" font-size="100">HARROW</text>
  <text class="sign-text centred company-name" x="600" y="225" font-size="100">STITCH</text>
  <text class="sign-text centred company-trade" x="600" y="320" font-size="57">&amp; EMBROIDERY</text>

  <!-- Message -->
  <text class="sign-text centred message-lead" x="600" y="410" font-size="64">YOUR LOGO</text>
  <text class="sign-text centred message-lead" x="600" y="478" font-size="64">EMBROIDERY</text>

  <text class="sign-text centred message-distance" x="600" y="564" font-size="80">ONE MILE</text>
  <g class="arrow-down">
    <rect class="icon-white" x="406" y="589" width="18" height="30"/>
    <polygon class="icon-white" points="387,617 443,617 415,646"/>
  </g>
  <text class="sign-text centred message-distance" x="600" y="646" font-size="80">AHEAD</text>
  <g class="arrow-down">
    <rect class="icon-white" x="776" y="589" width="18" height="30"/>
    <polygon class="icon-white" points="757,617 813,617 785,646"/>
  </g>

  <!-- Address -->
  <g class="location-pin">
    <path class="icon-white" d="M414,714 L400,699 A18,18 0 1 1 428,699 Z"/>
    <circle class="icon-cut" cx="414" cy="688" r="7"/>
  </g>
  <text class="sign-text address" x="444" y="712" font-size="54">12 Corvel way</text>
  <text class="sign-text centred address" x="600" y="764" font-size="54">EN4 7TR</text>
  <rect class="icon-white address-rule" x="380" y="772" width="440" height="5"/>
</svg>
</body>
</html>
```